Local fast-growing company in the service sector

We are looking for a modern business card design, which should also appear on our letterheads

Target Market(s)

Private and industrial sectors

Contact Information for Business Card

Vorname Name
Lindkofer Str. 18
71468 Remsbachtal
Tel.: 07163-418259-0
Name@kovaltec-pbz.de

Colors
9d9d9d
919191
aaaaaa

Requirements
Must have
• The logo (file) in silver

```html
<!DOCTYPE html>
<html lang="de">
<head>
<meta charset="utf-8">
<title>KOVALTEC – Visitenkarte</title>
<link href="https://fonts.googleapis.com/css2?family=Open+Sans:wght@400;600;700&display=swap" rel="stylesheet">
<style>
  :root {
    --stage: #e6e6e6;
    --card: #ffffff;
    --silver: #9d9d9d;
    --silver-mid: #919191;
    --silver-light: #aaaaaa;
    --ink: #5a5a5a;
    --ink-dark: #444444;
    --map: #f1f1f1;
    --icon: #888888;
  }
  * { box-sizing: border-box; margin: 0; padding: 0; }
  html, body {
    width: 1200px; height: 907px; overflow: hidden;
    background: var(--stage);
    font-family: "Open Sans", Arial, sans-serif;
  }
  .stage {
    position: relative; width: 1200px; height: 907px;
    display: flex; align-items: center; justify-content: center; gap: 40px;
  }
  .card {
    position: relative; width: 540px; height: 350px;
    background: var(--card);
    box-shadow: 0 8px 22px rgba(0,0,0,.14);
    overflow: hidden;
  }
  .world-map {
    position: absolute; left: 50px; top: 40px; width: 440px; height: 260px;
    background: radial-gradient(ellipse at center, var(--map) 0%, rgba(241,241,241,.4) 70%, rgba(255,255,255,0) 100%);
  }
  /* Front */
  .holder-name {
    position: absolute; left: 34px; top: 210px;
    font-weight: 700; font-size: 24px; color: var(--ink);
  }
  .brand-mark {
    position: absolute; left: 200px; top: 128px;
    display: flex; align-items: center; gap: 8px;
    font-weight: 700; font-size: 20px; color: var(--silver);
  }
  .brand-mark .dot { width: 14px; height: 14px; border-radius: 50%; background: var(--silver-light); }
  .contact {
    position: absolute; left: 350px; top: 110px; width: 170px;
    font-style: normal;
    font-size: 12.5px; line-height: 20px; color: var(--ink);
    white-space: nowrap;
  }
  .contact .company { font-weight: 700; color: var(--ink-dark); }
  .contact .line { display: flex; align-items: center; gap: 5px; }
  .contact svg { width: 12px; height: 12px; flex: none; }
  /* Back */
  .back-brand {
    position: absolute; left: 110px; top: 130px;
  }
  .back-brand .wordmark {
    display: flex; align-items: center; gap: 12px;
    font-weight: 700; font-size: 52px; line-height: 1; color: var(--silver);
    letter-spacing: -1px;
  }
  .back-brand .wordmark .square { width: 34px; height: 34px; background: var(--silver-light); }
  .back-brand .web {
    margin-left: 46px; margin-top: 6px;
    font-size: 20px; color: var(--silver-mid); letter-spacing: 1px;
  }
</style>
</head>
<body>
<main class="stage">
  <section class="card card-front">
    <div class="world-map" role="img" aria-label="Faint dotted world map in the background"></div>
    <p class="holder-name">Vorname Name</p>
    <div class="brand-mark"><span class="dot"></span>KOVALTEC</div>
    <address class="contact">
      <div class="company">KOVALTEC</div>
      <div>Lindkofer Str. 18</div>
      <div>71468 Remsbachtal</div>
      <div class="line">
        <svg viewBox="0 0 12 12" aria-hidden="true"><circle cx="6" cy="6" r="6" fill="var(--icon)"/><path d="M3.8 3.2l1 .1.5 1.4-.7.6a4 4 0 0 0 2 2l.6-.7 1.4.5.1 1c-2.6.6-5.4-2.2-4.9-4.9z" fill="#fff"/></svg>
        07163-418259-0
      </div>
      <div class="line">
        <svg viewBox="0 0 12 12" aria-hidden="true"><circle cx="6" cy="6" r="6" fill="var(--icon)"/><rect x="3" y="4" width="6" height="4.2" fill="none" stroke="#fff" stroke-width=".9"/><path d="M3 4l3 2.3L9 4" fill="none" stroke="#fff" stroke-width=".9"/></svg>
        Name@kovaltec-pbz.de
      </div>
    </address>
  </section>

  <section class="card card-back">
    <div class="world-map" role="img" aria-label="Faint dotted world map in the background"></div>
    <div class="back-brand">
      <div class="wordmark"><span class="square"></span>KOVALTEC</div>
      <div class="web">kovaltec-pbz.de</div>
    </div>
  </section>
</main>
</body>
</html>
```